Business card for consulting firm

We need a double-sided business card for consulting firm, VantorQ. The card should be professional but also creative and visually interesting.

Target Market(s)

Engineering and technology; transport industries; safety critical / heavy industry.

Contact Information for Business Card

See attached file with details.

Font styles to use
Sans Serif

```html
<!DOCTYPE html>
<html lang="en">
<head>
<meta charset="utf-8">
<title>VantorQ Business Card</title>
<link href="https://fonts.googleapis.com/css2?family=Open+Sans:wght@400;600;700&display=swap" rel="stylesheet">
<style>
  :root {
    --backdrop: #2d2522;
    --card-white: #f7f7f8;
    --brand-purple: #97308f;
    --brand-navy: #2b1f5c;
    --text-purple: #6b3f92;
    --divider: #c9c4d4;
  }
  * { margin: 0; padding: 0; box-sizing: border-box; }
  html, body {
    width: 1200px; height: 844px; overflow: hidden;
    background: var(--backdrop);
    font-family: "Open Sans", Arial, sans-serif;
  }
  .stage {
    position: relative; width: 1200px; height: 844px;
    display: flex; align-items: center; justify-content: center; gap: 60px;
  }
  .card {
    width: 510px; height: 292px; border-radius: 3px;
    box-shadow: 0 10px 24px rgba(0,0,0,.45);
    position: relative;
  }
  .card-front { background: var(--card-white); color: var(--brand-navy); text-align: center; }
  .card-back {
    background: var(--brand-purple); color: #fff;
    display: flex; align-items: center; justify-content: center;
  }

  .wordmark { display: inline-block; text-align: left; }
  .wordmark-name {
    display: flex; align-items: center; gap: 8px;
    font-weight: 700; letter-spacing: 1px; line-height: 1;
  }
  .wordmark-dot { border-radius: 50%; flex: none; }
  .wordmark-tagline { font-weight: 400; line-height: 1; }

  .card-front .wordmark { margin-top: 36px; }
  .card-front .wordmark-name { font-size: 40px; color: var(--brand-navy); }
  .card-front .wordmark-dot { width: 12px; height: 12px; background: var(--brand-purple); }
  .card-front .wordmark-tagline { font-size: 15px; color: var(--text-purple); margin: 4px 0 0 20px; }

  .card-back .wordmark-name { font-size: 56px; color: #fff; }
  .card-back .wordmark-dot { width: 16px; height: 16px; background: #fff; }
  .card-back .wordmark-tagline { font-size: 20px; color: #fff; margin: 6px 0 0 26px; }

  .holder { margin-top: 20px; }
  .holder-name { font-size: 17px; font-weight: 600; color: var(--brand-purple); letter-spacing: .3px; }
  .holder-credentials, .holder-role { font-size: 12px; color: var(--text-purple); line-height: 1.5; }

  .contacts {
    margin-top: 18px; display: flex; justify-content: center; align-items: stretch;
    font-size: 13.5px; color: var(--brand-navy);
  }
  .contact-column { display: flex; flex-direction: column; gap: 6px; padding: 0 10px; }
  .contact-column.direct { align-items: flex-end; border-right: 1px solid var(--divider); }
  .contact-column.web { align-items: flex-start; }
  .contact-item { display: flex; align-items: center; gap: 5px; white-space: nowrap; }
  .contact-icon { width: 11px; height: 11px; fill: var(--brand-purple); flex: none; }
</style>
</head>
<body>
<main class="stage">
  <section class="card card-front">
    <div class="wordmark">
      <div class="wordmark-name"><span class="wordmark-dot"></span>VANTORQ</div>
      <div class="wordmark-tagline">Safety &amp; Human Factors</div>
    </div>

    <div class="holder">
      <p class="holder-name">MEGAN HARTLEY</p>
      <p class="holder-credentials">BSc (Hons), MA Org Psych, M Eng Sys (HF)</p>
      <p class="holder-role">Principal Consultant</p>
    </div>

    <div class="contacts">
      <div class="contact-column direct">
        <span class="contact-item">+61 (0)400 555 018
          <svg class="contact-icon" viewBox="0 0 12 12" aria-hidden="true"><path d="M1 3.5C1 2 2.5 1 6 1s5 1 5 2.5V5H8.5V4h-5v1H1z M2.5 6h7l1 4.5h-9z"/></svg>
        </span>
        <span class="contact-item">mhartley@vantorq.com.au
          <svg class="contact-icon" viewBox="0 0 12 12" aria-hidden="true"><path d="M0.5 2.5h11v7h-11z M1.2 3.2 6 6.8l4.8-3.6" stroke="#fff" stroke-width=".8"/></svg>
        </span>
      </div>
      <div class="contact-column web">
        <span class="contact-item">
          <svg class="contact-icon" viewBox="0 0 12 12" aria-hidden="true"><circle cx="6" cy="6" r="5.5"/><path d="M1 6h10M6 .8c-2 2.8-2 7.6 0 10.4M6 .8c2 2.8 2 7.6 0 10.4" stroke="#fff" stroke-width=".7" fill="none"/></svg>
          www.vantorq.global</span>
        <span class="contact-item">
          <svg class="contact-icon" viewBox="0 0 12 12" aria-hidden="true"><circle cx="6" cy="6" r="5.5"/><path d="M1 6h10M6 .8c-2 2.8-2 7.6 0 10.4M6 .8c2 2.8 2 7.6 0 10.4" stroke="#fff" stroke-width=".7" fill="none"/></svg>
          www.vantorq.com.au</span>
      </div>
    </div>
  </section>

  <section class="card card-back">
    <div class="wordmark">
      <div class="wordmark-name"><span class="wordmark-dot"></span>VANTORQ</div>
      <div class="wordmark-tagline">Safety &amp; Human Factors</div>
    </div>
  </section>
</main>
</body>
</html>
```